Business Card for Dental Surgery

Professional and vibrant business card for dental surgery

Other side to incorporate space for appointment date and times

My website is www.tallowbydental.com.au

Target Market(s)

All

Industry/Entity Type

Dental

Requirements
Must have
• Catchy
Phone no, internet etc
Nice to have
• portray same image as website.
on reverse appointment side:
"Please give 24 hours notice if you cannot attend"
Nice colours

```html
<!DOCTYPE html>
<html lang="en">
<head>
<meta charset="utf-8">
<title>Tallowby Dental – Business Card</title>
<link rel="stylesheet" href="https://fonts.googleapis.com/css2?family=Arimo:wght@400;700&display=swap">
<style>
  :root {
    --backdrop: #cfcecf;
    --card: #ffffff;
    --card-edge: #e4e3e5;
    --panel: #dcdcdd;
    --panel-glow: #f1f1f2;
    --band: #6f7276;
    --ink: #6d6e71;
    --ink-soft: #808285;
    --brand: #93318f;
    --icon-phone: #7cc242;
    --icon-mobile: #f7a823;
    --icon-fax: #8a8c8f;
    --icon-mail: #d63fcb;
  }
  * { box-sizing: border-box; margin: 0; padding: 0; }
  html, body { width: 1200px; height: 765px; overflow: hidden; }
  body {
    background: var(--backdrop);
    font-family: "Arimo", Arial, sans-serif;
    color: var(--ink);
    position: relative;
  }
  .card {
    position: absolute;
    top: 302px;
    width: 574px;
    height: 343px;
    border-radius: 42px;
    background: radial-gradient(ellipse at 50% 40%, var(--card) 40%, var(--card-edge) 100%);
    overflow: hidden;
  }
  .card--front { left: 16px; }
  .card--back { left: 604px; }

  .brand-name {
    color: var(--brand);
    font-weight: 700;
    letter-spacing: -1px;
    white-space: nowrap;
  }
  .card--front .brand-name {
    position: absolute;
    left: 0; right: 0;
    top: 130px;
    text-align: center;
    font-size: 42px;
  }

  .appointment-panel {
    position: absolute;
    left: 22px; top: 25px;
    width: 532px; height: 172px;
    background: radial-gradient(ellipse at 70% 45%, var(--panel-glow) 0%, var(--panel) 70%);
  }
  .holder-name {
    position: absolute;
    right: 45px; top: 60px;
    font-size: 34px;
    font-weight: 700;
    color: var(--ink);
    letter-spacing: -0.5px;
  }
  .holder-title {
    position: absolute;
    right: 45px; top: 96px;
    font-size: 17px;
    color: var(--ink);
  }
  .notice {
    position: absolute;
    left: 14px; bottom: 6px;
    font-size: 12px;
    color: var(--ink-soft);
  }
  .notice strong { color: var(--ink); }
  .divider-band {
    position: absolute;
    left: 22px; top: 197px;
    width: 532px; height: 11px;
    background: var(--band);
  }
  .card--back .brand-name {
    position: absolute;
    left: 36px; top: 210px;
    font-size: 20px;
    letter-spacing: -0.5px;
  }
  .website {
    position: absolute;
    left: 37px; top: 235px;
    font-size: 11px;
    letter-spacing: 2px;
    color: var(--brand);
  }
  .contact-list {
    position: absolute;
    right: 38px; top: 216px;
    list-style: none;
    text-align: right;
  }
  .contact-item {
    display: flex;
    justify-content: flex-end;
    align-items: center;
    gap: 10px;
    height: 21px;
    font-size: 18px;
    color: var(--ink);
    letter-spacing: 0.5px;
  }
  .contact-item--email { font-size: 14px; letter-spacing: 0.3px; }
  .contact-icon { width: 16px; height: 16px; flex: none; }
</style>
</head>
<body>
  <section class="card card--front" aria-label="Card front">
    <div class="brand-name">Tallowby Dental</div>
  </section>

  <section class="card card--back" aria-label="Card back">
    <div class="appointment-panel">
      <div class="holder-name">JOHN DOE</div>
      <div class="holder-title">Job Title</div>
      <p class="notice">Please give <strong>24 hours</strong> notice if you cannot attend</p>
    </div>
    <div class="divider-band"></div>

    <div class="brand-name">Tallowby Dental</div>
    <div class="website">www.tallowbydental.com.au</div>

    <ul class="contact-list">
      <li class="contact-item">00 123 4567 890
        <svg class="contact-icon" viewBox="0 0 16 16" aria-label="Phone"><rect width="16" height="16" rx="3" fill="var(--icon-phone)"/><path d="M4 7h8v4H4zM3.5 6.5c1-2 8-2 9 0" fill="none" stroke="#fff" stroke-width="1.4"/></svg>
      </li>
      <li class="contact-item">00 123 4567 890
        <svg class="contact-icon" viewBox="0 0 16 16" aria-label="Mobile"><rect width="16" height="16" rx="3" fill="var(--icon-mobile)"/><rect x="5" y="3" width="6" height="10" rx="1" fill="none" stroke="#fff" stroke-width="1.4"/></svg>
      </li>
      <li class="contact-item">00 123 4567 890
        <svg class="contact-icon" viewBox="0 0 16 16" aria-label="Fax"><rect width="16" height="16" rx="3" fill="var(--icon-fax)"/><rect x="4" y="3" width="8" height="10" fill="none" stroke="#fff" stroke-width="1.4"/><path d="M6 8h4M6 10.5h4" stroke="#fff" stroke-width="1.2"/></svg>
      </li>
      <li class="contact-item contact-item--email">john.doe@tallowbydental.com
        <svg class="contact-icon" viewBox="0 0 16 16" aria-label="Email"><rect width="16" height="16" rx="3" fill="var(--icon-mail)"/><path d="M3.5 5h9v6.5h-9zM3.5 5l4.5 4 4.5-4" fill="none" stroke="#fff" stroke-width="1.3"/></svg>
      </li>
    </ul>
  </section>
</body>
</html>
```